Creative Law Firm Business Card

attached are photos of myself and our office as well as language that I would like to see on the card, likely on the back, although I leave that to the designer. I have also attached copies of both sides of a marketing card that we produced just for ideas. I would like to find a tactful way to get my photo in along with the office. I attached copies of our logo, both normal and inverted.

I listed my name as Glen Whitacre to be casual, however, it should probably read Glenford T Whitacre

Requirements
Must have
• attached file #8 has content.
• I would like my picture and the office photo on page 1
• The text, with the exception of the firm name "WHITACRE & LOMAX" and the firm description underneath it "THE BUSINESS AND BANKRUPTCY LAWYERS", should be on the back. The layout and fonts are up to the designer

```html
<!DOCTYPE html>
<html lang="en">
<head>
<meta charset="utf-8">
<title>Whitacre &amp; Lomax – Business Card</title>
<link rel="stylesheet" href="https://fonts.googleapis.com/css2?family=Cinzel:wght@400;600&family=Arimo:wght@400&display=swap">
<style>
  :root {
    --page: #ececec;
    --slate: #4f5f7a;
    --paper: #ffffff;
    --blue: #1f5d93;
    --blue-deep: #0f3a66;
    --portrait-light: #5b8fc0;
    --portrait-mid: #1d4d80;
    --portrait-dark: #15171c;
    --sepia-light: #d9c79a;
    --sepia-mid: #a8915e;
    --sepia-dark: #6f5c36;
    --mark: #8d99ad;
    --gold: #c9a55a;
    --white: #ffffff;
  }
  * { box-sizing: border-box; margin: 0; padding: 0; }
  html, body { width: 1002px; height: 1200px; overflow: hidden; background: var(--page); }
  .sheet {
    width: 1002px; height: 1200px;
    display: flex; flex-direction: column; align-items: center; justify-content: center;
    gap: 80px;
  }
  .card {
    position: relative; width: 760px; height: 434px; overflow: hidden;
    box-shadow: 0 2px 6px rgba(0,0,0,.18);
  }

  /* Front */
  .card-front { background: var(--blue); }
  .card-front .art { position: absolute; inset: 0; }
  .identity {
    position: absolute; left: 372px; top: 282px; color: var(--white);
  }
  .identity .name {
    font-family: "Cinzel", serif; font-weight: 600; font-size: 28px; letter-spacing: .5px; line-height: 1;
  }
  .identity .title {
    font-family: "Arimo", sans-serif; font-size: 12px; letter-spacing: .4px; margin-top: 8px;
  }
  .identity .experience {
    font-family: "Arimo", sans-serif; font-size: 11px; margin-top: 2px;
  }
  .identity .contact {
    font-family: "Arimo", sans-serif; font-size: 14px; line-height: 1.3; margin-top: 18px;
  }

  /* Back */
  .card-back { background: var(--paper); display: flex; flex-direction: column; }
  .band-top {
    height: 118px; background: var(--slate);
    display: flex; flex-direction: column; align-items: center; justify-content: flex-end;
    gap: 10px; padding-bottom: 12px;
  }
  .firm-mark { width: 34px; height: 34px; background: var(--white); }
  .firm-name {
    font-family: "Cinzel", serif; font-weight: 400; font-size: 22px; color: var(--white); letter-spacing: 1px;
    padding-top: 6px; border-top: 1px solid var(--white);
  }
  .practice-areas {
    flex: 1; list-style: none; text-align: center;
    display: flex; flex-direction: column; justify-content: center;
    font-family: "Cinzel", serif; font-size: 14px; line-height: 1.45; color: var(--slate); letter-spacing: .3px;
  }
  .band-bottom {
    height: 108px; background: var(--slate); color: var(--white);
    display: flex; flex-direction: column; justify-content: center; align-items: center;
    font-family: "Arimo", sans-serif; font-size: 18px; line-height: 1.55;
  }
</style>
</head>
<body>
<main class="sheet">

  <section class="card card-front">
    <svg class="art" width="760" height="434" viewBox="0 0 760 434">
      <defs>
        <linearGradient id="field" x1="0" y1="0" x2="1" y2="1">
          <stop offset="0" stop-color="var(--blue)"/>
          <stop offset="1" stop-color="var(--blue-deep)"/>
        </linearGradient>
        <linearGradient id="office" x1="0" y1="0" x2="1" y2="1">
          <stop offset="0" stop-color="var(--sepia-dark)"/>
          <stop offset=".45" stop-color="var(--sepia-light)"/>
          <stop offset=".75" stop-color="var(--sepia-mid)"/>
          <stop offset="1" stop-color="var(--sepia-dark)"/>
        </linearGradient>
        <linearGradient id="portrait" x1="0" y1="0" x2="0" y2="1">
          <stop offset="0" stop-color="var(--portrait-light)"/>
          <stop offset=".45" stop-color="var(--portrait-mid)"/>
          <stop offset=".6" stop-color="var(--portrait-dark)"/>
          <stop offset="1" stop-color="var(--portrait-dark)"/>
        </linearGradient>
      </defs>
      <rect class="field" width="760" height="434" fill="url(#field)"/>
      <path class="office-photo" role="img" aria-label="Photo of the firm's office building with palm trees, sepia toned"
            d="M230,0 H760 V236 C620,228 480,240 362,270 C336,180 296,80 230,0 Z" fill="url(#office)"/>
      <rect class="firm-mark-faint" x="470" y="40" width="130" height="130" fill="var(--mark)" opacity=".75"/>
      <path class="portrait-frame" d="M0,0 H226 C310,110 352,250 336,434 H0 Z" fill="none" stroke="var(--gold)" stroke-width="5"/>
      <path class="portrait-photo" role="img" aria-label="Portrait photo of Glenford T Whitacre in a dark suit"
            d="M0,0 H220 C302,110 342,250 326,434 H0 Z" fill="url(#portrait)"/>
    </svg>
    <div class="identity">
      <p class="name">Glenford T Whitacre</p>
      <p class="title">STATE BAR CERTIFIED BANKRUPTCY SPECIALIST</p>
      <p class="experience">36 years experience - AV Grade</p>
      <p class="contact">714.555.0142<br>glen@whitacrelomax.com</p>
    </div>
  </section>

  <section class="card card-back">
    <header class="band-top">
      <span class="firm-mark"></span>
      <p class="firm-name">WHITACRE &amp; LOMAX</p>
    </header>
    <ul class="practice-areas">
      <li>Business Litigation</li>
      <li>Debtor &amp; Creditor Bankruptcy and Insolvency Matters</li>
      <li>Corporate Reorganizations</li>
      <li>Commercial Landlord - Tenant Transactional</li>
      <li>and Litigation Matters</li>
      <li>Business Formations</li>
      <li>Mediation</li>
      <li>AV Rated</li>
    </ul>
    <footer class="band-bottom">
      <p class="address">1280 Alder Crest Rd Irvine, CA 92618</p>
      <p class="web">www.whitacrelomax.com</p>
    </footer>
  </section>

</main>
</body>
</html>
```